Business Card & Stationary Design Project

We are looking for some creative direction for business cards and our stationary.

We are a global logistics firm that has recently changed its name to Marrick Global Logistics and we have a new website due out tomorrow (www.marrick.com.au).

The colours of the company are rich navy tones, I would like to have business cards that fit together to make one picture on the back (possibly an old map of the world??), and the front to be modern contemporary looking.

But I am open to suggestions, so just incorporate our new logo and get going!
Updates

Hi Everyone,

Thank you for all of your designs so far and the time you have put into it.

I have asked many of you for amendments to see if we can get a final product, so with this in mind I am extending the deadline by a few days.

Good luck and thank you once again.

Please message me direct if you need any clarification.

Kind Regards
Colin

Reason: As outlined the extra 3 days is for amendments and changes to the current submissions. Thanks Colin

Industry/Entity Type

Business

```html
<!DOCTYPE html>
<html lang="en">
<head>
<meta charset="utf-8">
<title>Marrick Global Logistics – Business Card</title>
<link rel="stylesheet" href="https://fonts.googleapis.com/css2?family=Questrial&display=swap">
<style>
  :root {
    --page-bg: #f4f6f7;
    --card-edge: #3dbdca;
    --card-mid: #8fd9e1;
    --card-light: #eefafb;
    --map-tone: #3aa5b3;
    --navy: #10247a;
    --ink: #111111;
    --bar: #0b0b0b;
    --bar-text: #e8e8e8;
  }
  * { margin: 0; padding: 0; box-sizing: border-box; }
  html, body {
    width: 1200px; height: 1000px; overflow: hidden;
    background: var(--page-bg);
  }
  .canvas {
    position: relative; width: 1200px; height: 1000px;
  }
  .business-card {
    position: absolute; left: 150px; top: 243px;
    width: 900px; height: 514px; overflow: hidden;
    background:
      radial-gradient(ellipse 560px 380px at 560px 120px, var(--card-light) 0%, var(--card-mid) 55%, var(--card-edge) 100%);
    box-shadow: 0 6px 24px rgba(0,0,0,0.18);
    font-family: "Questrial", "Century Gothic", sans-serif;
    color: var(--ink);
  }
  .world-map-area {
    position: absolute; left: 0; top: 0; width: 390px; height: 514px;
    background: radial-gradient(ellipse 200px 280px at 180px 250px, rgba(58,165,179,0.45), rgba(58,165,179,0) 75%);
  }
  .brand {
    position: absolute; right: 183px; top: 58px; text-align: right;
    color: var(--navy); font-weight: 400;
  }
  .brand-name {
    font-size: 44px; letter-spacing: 14px; line-height: 1;
    margin-right: -14px;
  }
  .brand-tagline {
    font-size: 14px; letter-spacing: 6px; margin-top: 6px; margin-right: -6px;
  }
  .brand-mark {
    position: absolute; left: 744px; top: 18px; width: 140px; height: 140px;
  }
  .address {
    position: absolute; right: 40px; top: 202px;
    text-align: right; font-size: 19px; line-height: 25px;
  }
  .contact {
    position: absolute; right: 40px; top: 346px;
    text-align: right; font-size: 19px; line-height: 25px;
  }
  .contact b { font-weight: 700; margin: 0 12px 0 28px; }
  .contact .gap { display: inline-block; width: 24px; }
  .web-bar {
    position: absolute; left: 0; top: 471px; width: 430px; height: 41px;
    background: var(--bar); color: var(--bar-text);
    font-size: 18px; line-height: 41px; padding-left: 26px;
  }
</style>
</head>
<body>
<div class="canvas">
  <section class="business-card">
    <div class="world-map-area" role="img" aria-label="Faint world map showing North and South America"></div>

    <div class="brand">
      <div class="brand-name">MARRICK</div>
      <div class="brand-tagline">Global Logistics</div>
    </div>
    <svg class="brand-mark" viewBox="0 0 140 140" aria-hidden="true">
      <circle cx="70" cy="70" r="70" fill="var(--navy)"/>
    </svg>

    <address class="address" style="font-style:normal">
      58 Harbour Lane<br>
      Pyrmont<br>
      NSW 2009
    </address>

    <div class="contact">
      <div><b>P</b>02 9100 4200<b>M</b>0400555210</div>
      <div><b>F</b>029100 4299</div>
      <div><b>E</b>colin@marrick.com.au</div>
    </div>

    <div class="web-bar">www.marrick.com.au</div>
  </section>
</div>
</body>
</html>
```